Create a hero image for my construction company

We are a large construction company in Australia and would like to find a long term partner to help us develop our brand. To start we will upload 4 recent images (low quality from our company Whats App). Edit 1 or all of these images to create an edgy magazine/movie poster style image. These images are just concepts to show management. Please get creative. Happy editing. Thanks

Target Market(s)

Large Construction Companies and Builders

Font styles to use
Sans Serif

Colors

Designer to choose colors to be used in the design.

```html
<!DOCTYPE html>
<html lang="en">
<head>
<meta charset="utf-8">
<title>Kestrel Ridge – Construction Company</title>
<link rel="stylesheet" href="https://fonts.googleapis.com/css2?family=Open+Sans:wght@400;600;700;800&display=swap">
<style>
  :root {
    --white: #ffffff;
    --sun: #f7c948;
    --amber: #f2a54a;
    --orange: #f07a2c;
    --flame: #ff4a1c;
    --clay: #e9a064;
    --teal: #27d3c0;
    --lime: #8fd46a;
    --ink: #3b2a1a;
  }
  * { margin: 0; padding: 0; box-sizing: border-box; }
  html, body { width: 1200px; height: 800px; overflow: hidden; background: #fff; }
  body { font-family: "Open Sans", Arial, sans-serif; color: var(--white); }

  .hero { position: relative; width: 1200px; height: 800px; overflow: hidden; }

  .hero__photo {
    position: absolute; inset: 0;
    background:
      radial-gradient(ellipse 420px 320px at 640px 470px, rgba(39,211,192,0.55), rgba(39,211,192,0) 70%),
      linear-gradient(180deg, #f5c55a 0%, #f2b45a 35%, #eea262 60%, #eb9a5e 100%);
  }

  .hero__shapes { position: absolute; inset: 0; width: 1200px; height: 800px; }

  .brand { position: absolute; left: 46px; top: 46px; }
  .brand__cross { width: 58px; height: 58px; display: block; }
  .brand__rule { width: 393px; height: 5px; background: var(--white); margin: 28px 0 0 34px; }
  .brand__name {
    font-weight: 800; font-size: 72px; line-height: 1; letter-spacing: -1px;
    text-transform: uppercase; margin-top: 4px; white-space: nowrap;
  }
  .brand__sub {
    font-weight: 800; font-size: 30px; line-height: 1; margin-top: 10px; white-space: nowrap;
  }

  .presents {
    position: absolute; left: 540px; top: 44px; width: 120px; text-align: center;
    font-weight: 700; font-size: 15px; letter-spacing: 1px; line-height: 1.1;
  }
  .presents span { display: block; font-weight: 400; font-size: 11px; letter-spacing: 0.5px; }

  .event { position: absolute; left: 38px; top: 588px; }
  .event__days { font-size: 40px; font-weight: 400; line-height: 1.1; }
  .event__month { font-size: 29px; font-weight: 400; line-height: 1.2; }
  .event__title { font-size: 31px; font-weight: 700; line-height: 1.3; margin-top: 8px; letter-spacing: 0.5px; }

  .website { position: absolute; right: 36px; bottom: 30px; font-size: 13px; opacity: 0.9; }
</style>
</head>
<body>
<main class="hero">
  <div class="hero__photo" role="img" aria-label="Drilling rig on tracks working in an excavated construction site in front of an apartment building, tinted orange and teal"></div>

  <svg class="hero__shapes" viewBox="0 0 900 600" aria-hidden="true">
    <defs>
      <linearGradient id="frameWarm" x1="0" y1="0" x2="1" y2="1">
        <stop offset="0" stop-color="#f7b23a"/>
        <stop offset="1" stop-color="#ff3d17"/>
      </linearGradient>
      <linearGradient id="frameCool" x1="0" y1="0" x2="1" y2="1">
        <stop offset="0" stop-color="#a6e07a"/>
        <stop offset="0.5" stop-color="#f2b440"/>
        <stop offset="1" stop-color="#ff4a1c"/>
      </linearGradient>
      <linearGradient id="triFill" x1="0" y1="0" x2="0" y2="1">
        <stop offset="0" stop-color="#8fd46a" stop-opacity="0.45"/>
        <stop offset="1" stop-color="#1fd6d0" stop-opacity="0.85"/>
      </linearGradient>
    </defs>

    <polygon class="shape-prism" points="395,0 545,595 735,360 470,160" fill="url(#triFill)"/>
    <polyline class="frame-line" points="415,0 545,595 730,370" fill="none" stroke="#9be07a" stroke-width="7" opacity="0.85"/>
    <polygon class="frame-square" points="400,20 880,25 795,505 350,215" fill="none" stroke="url(#frameWarm)" stroke-width="11" opacity="0.9"/>
    <polygon class="frame-tilt" points="330,408 470,130 890,170 640,465" fill="none" stroke="url(#frameCool)" stroke-width="10" opacity="0.85"/>
    <polyline class="frame-accent" points="720,320 655,600" fill="none" stroke="#ff3d17" stroke-width="10"/>

    <g class="chevrons" fill="none" stroke="#ffffff" stroke-width="5" stroke-linejoin="miter">
      <polyline points="30,338 48,360 30,382"/>
      <polyline points="60,338 78,360 60,382"/>
      <polyline points="90,338 108,360 90,382"/>
      <polyline points="120,338 138,360 120,382"/>
      <polyline points="150,338 168,360 150,382"/>
      <polyline points="180,338 198,360 180,382"/>
      <polyline points="210,338 228,360 210,382"/>
      <polyline points="240,338 258,360 240,382"/>
    </g>
  </svg>

  <header class="brand">
    <svg class="brand__cross" viewBox="0 0 58 58" aria-hidden="true">
      <path d="M6 6 L52 52 M52 6 L6 52" stroke="#ffffff" stroke-width="12" stroke-linecap="square"/>
    </svg>
    <div class="brand__rule"></div>
    <h1 class="brand__name">Kestrel Ridge</h1>
    <p class="brand__sub">Builders &nbsp;1300 Earthworks</p>
  </header>

  <p class="presents">KESTREL RIDGE<span>PRESENTS</span></p>

  <section class="event">
    <p class="event__days">24, 25</p>
    <p class="event__month">OCTOBER</p>
    <h2 class="event__title">CONSTRUCTION<br>COMPANY</h2>
  </section>

  <p class="website">www.yourwebsite.com</p>
</main>
</body>
</html>
```